Commercial Piping Company Needs A Modern Business Card

We need a clean business card for our commercial pipe lining company. We would like to see a mock up in two color schemes: Black, Grey and Blue and Black, Grey and Orange. We are in the piping industry, but want a professional, clean and modern look to the card.

Industry/Entity Type

Plumbing

Contact Information for Business Card

Name: Mark Telford
Title: Managing Partner
Phone: 608.352.9174
Email: Mark@VeltaSpan.Net

Requirements
Must have
• Back Side Should Have a White Back Ground with Full Logo. Front I would like to see a couple lay outs for contact info. Also the final card will have rounded edges, so please take that into account for printing.
Nice to have
• Two Color Palette Examples
Should not have
• No need for an address line

```html
<!DOCTYPE html>
<html lang="en">
<head>
<meta charset="utf-8">
<title>VeltaSpan Business Card</title>
<link rel="stylesheet" href="https://fonts.googleapis.com/css2?family=Montserrat:wght@400;500;700;800&display=swap">
<style>
  :root {
    --bg-dark: #2b2c2e;
    --bg-light: #5a5b5e;
    --card-white: #ffffff;
    --brand-blue: #1f78c1;
    --band-dark: #333436;
    --stripe-grey: #b4b4b4;
    --text-light: #c9c9c9;
    --text-ink: #111111;
    --card-radius: 26px;
  }
  html, body {
    margin: 0;
    padding: 0;
    width: 1200px;
    height: 900px;
    overflow: hidden;
  }
  body {
    background: radial-gradient(ellipse at 60% 35%, var(--bg-light) 0%, var(--bg-dark) 70%);
    font-family: "Montserrat", Arial, sans-serif;
    position: relative;
  }
  .card {
    position: absolute;
    left: 280px;
    width: 640px;
    height: 366px;
    border-radius: var(--card-radius);
    overflow: hidden;
    box-shadow: 0 18px 40px rgba(0,0,0,0.45);
  }
  .card--back {
    top: 64px;
    background: var(--card-white);
    display: flex;
    align-items: center;
    justify-content: center;
  }
  .card--front {
    top: 470px;
    background: var(--brand-blue);
  }
  .card__art {
    position: absolute;
    inset: 0;
    width: 100%;
    height: 100%;
  }

  /* Back: brand name with plain mark */
  .brand {
    display: flex;
    align-items: center;
    gap: 18px;
  }
  .brand__mark {
    width: 72px;
    height: 72px;
    border-radius: 50%;
    background: var(--text-ink);
    flex: none;
  }
  .brand__name {
    font-weight: 700;
    font-size: 46px;
    letter-spacing: 1px;
    line-height: 1;
    color: var(--text-ink);
  }

  /* Front: brand block */
  .front-brand {
    position: absolute;
    right: 30px;
    top: 72px;
    width: 200px;
    text-align: center;
  }
  .front-brand__mark {
    width: 70px;
    height: 70px;
    border-radius: 50%;
    background: var(--brand-blue);
    margin: 0 auto 20px;
  }
  .front-brand__name {
    font-weight: 700;
    font-size: 29px;
    letter-spacing: 0.5px;
    line-height: 1;
    color: var(--text-light);
  }

  /* Front: person */
  .person {
    position: absolute;
    left: 48px;
    top: 150px;
    padding-left: 22px;
    border-left: 6px solid var(--stripe-grey);
  }
  .person__name {
    font-weight: 800;
    font-size: 25px;
    letter-spacing: 0.5px;
    color: var(--text-light);
    margin: 4px 0 6px;
  }
  .person__title {
    font-weight: 700;
    font-size: 18px;
    color: var(--text-light);
    margin: 0 0 6px;
  }

  /* Front: contacts */
  .contacts {
    position: absolute;
    left: 78px;
    top: 268px;
    list-style: none;
    margin: 0;
    padding: 0;
  }
  .contacts__item {
    display: flex;
    align-items: center;
    gap: 12px;
    font-weight: 700;
    font-size: 19px;
    color: var(--text-light);
    margin-bottom: 12px;
  }
  .contacts__icon {
    width: 20px;
    height: 20px;
    flex: none;
  }
</style>
</head>
<body>

  <section class="card card--back" aria-label="Business card back">
    <div class="brand">
      <div class="brand__mark"></div>
      <div class="brand__name">VELTASPAN</div>
    </div>
  </section>

  <section class="card card--front" aria-label="Business card front">
    <svg class="card__art" viewBox="0 0 640 366" preserveAspectRatio="none" aria-hidden="true">
      <defs>
        <path id="band-shape" d="M0,130 H360 C392,130 398,95 418,72 C430,60 445,55 470,55 H640 V275 H450 C415,275 405,240 372,240 H0 Z"/>
        <clipPath id="clip-left"><rect x="0" y="0" width="400" height="366"/></clipPath>
        <clipPath id="clip-right"><rect x="420" y="0" width="220" height="366"/></clipPath>
      </defs>
      <use href="#band-shape" fill="var(--stripe-grey)" transform="translate(0,-13)" clip-path="url(#clip-left)"/>
      <use href="#band-shape" fill="var(--stripe-grey)" transform="translate(0,14)" clip-path="url(#clip-right)"/>
      <use href="#band-shape" fill="var(--band-dark)"/>
    </svg>

    <div class="front-brand">
      <div class="front-brand__mark"></div>
      <div class="front-brand__name">VELTASPAN</div>
    </div>

    <div class="person">
      <p class="person__name">MARK TELFORD</p>
      <p class="person__title">Managing Partner</p>
    </div>

    <ul class="contacts">
      <li class="contacts__item">
        <svg class="contacts__icon" viewBox="0 0 20 20" aria-hidden="true">
          <rect x="6" y="1.5" width="8" height="17" rx="1.5" fill="none" stroke="var(--text-light)" stroke-width="1.6"/>
          <rect x="7.5" y="4" width="5" height="6" fill="var(--text-light)"/>
          <circle cx="10" cy="15.5" r="1" fill="var(--text-light)"/>
        </svg>
        <span>608.352.9174</span>
      </li>
      <li class="contacts__item">
        <svg class="contacts__icon" viewBox="0 0 20 20" aria-hidden="true">
          <rect x="1.5" y="5" width="17" height="11" rx="1" fill="none" stroke="var(--text-light)" stroke-width="1.6"/>
          <path d="M1.5 5 L10 11.5 L18.5 5" fill="none" stroke="var(--text-light)" stroke-width="1.6"/>
        </svg>
        <span>Mark@VeltaSpan.Net</span>
      </li>
    </ul>
  </section>

</body>
</html>
```